MODERN + COOL Business Card Needed!

SUMMARY
This is for a 40+ year old family business that is transitioning to the 2nd generation and is in real need of a more modern facelift. Ive attached a company logo (I made quickly as an idea with my limited PSD skills) to start off with that you are welcome to change and draw ideas from. Ive also attached some screen shots of cards I like to give you an idea of my preferences.

WHAT WE DO
The company name is Kin Dart HK Ltd. But I prefer to just call it Kin Dart or Kin Dart with Hong Kong as kind of a sub heading on the business card. We own a factory as well as help our customers find factories to make their product. Product I mean, toys 99.9% of the time. Simple old school toys like board games, puzzles, wooden toys, baby/infant toys.

You can say we are a "sourcing" or "trading" or "consulting" company with a factory to help you do it. But since we deal with toys, i like to keep it modern and cool and fun, not serious like managing hedge funds.

WHAT WE ARE LOOKING FOR
A cool, unique looking business card that stands out. In terms of design, something modern and professional. I like darker colored cards and I like colors such as blue/green/dark gray, but am open to other colored themes. I Like bright lime green with gray, always though thats a nice combo. I prefer cards that are all colored and not so much white showing (I think). Ive attached a few screenshots of cards so take a look to get a feel of what I like.

We do alot of wooden stacking games in variety of colors too like Pulto, Roni, Torvanets (google these to check them out). So designs that sort of resemble stacking or building would be cool but totally not necessary.

In terms of the physical aspects of the card, Im looking for a card a bit different than the standard rectangular shape. Double sided. Little things like having corner(s) be round or different angle instead of square edge I always thought was nice. Its got to be mostly a normal card size, no folding or smaller cards that fit weird in your wallet. No vertical designs. Am open to VERY different/creative shapes (as long as it still fits in a wallet good like a normal buisness card.

Hi everyone!

Just wanted to write a message to everyone to let them know all submissions are being reviewed or have been reviewed.  If I have not responded with feedback, rest assure your submission was definitely looked at in detail but I either have just been too busy to respond (alot of submissions!), or its on my to be considered list.

I respect and really enjoy receiving everyones creativity and work so I dont want it to go unrecognized - thus this message!  Feel free to submit more ideas if you like until this project ends.  Sometimes some designs just dont click but sometimes they can so you never know!

Thanks again for everyones participation and great work!

~Dov Ruel

Target Market(s)

The cards are mainly handed to toy company sourcers and buyers. People I talk to ... say Quelvin for example... might want to make their next edition of Farthundle game with a reputable factory at a good cost so they can sell it to stores at a profit.

So these are the types of people I often try to talk and introduce myself and my company to.

Industry/Entity Type

Building

Colors
acd036
0392cd
00a88e
474747
606060

Requirements
Must have
• Just double sided, not plain rectangle corners, and just cool to look at and catches your eye!

Oh and the obvious business card stuff like place for name, address, number, email, etc.
Nice to have
• Think more modern and fun, not serious and old fashion (thats what we used to be!). Can use the logo I attached and you can definitely alter and change the logo or make a whole new one!

Oh and can definitely use a creative slogan if you like to think of one based on what I described in what we do.
Should not have
• Dont use fonts or text placement that might make "Kin Dart" look like "Kind Art"... We arent selling news papers!!

Please nothing related to education since we have the word Dart in the title, thats not our business at all.

Logo and design should not be too heavy on things related to toys, as though thats what we primarily focus on now, what we do may change over time.

```html
<!DOCTYPE html>
<html lang="en">
<head>
<meta charset="utf-8">
<title>Kin Dart Hong Kong – Business Card</title>
<link rel="stylesheet" href="https://fonts.googleapis.com/css2?family=Cabin:wght@400;600;700&display=swap">
<style>
  :root {
    --backdrop: #2c2c2c;
    --card: #474747;
    --lime: #acd036;
    --teal: #00a88e;
    --ink: #f2f2f2;
    --radius: 20px;
  }
  * { margin: 0; padding: 0; box-sizing: border-box; }
  html, body { width: 1200px; height: 900px; overflow: hidden; }
  body {
    background: var(--backdrop);
    font-family: "Cabin", "Gill Sans", sans-serif;
    position: relative;
  }
  .card {
    position: absolute;
    top: 301px;
    width: 513px;
    height: 296px;
    background: var(--card);
    border-radius: var(--radius);
    overflow: hidden;
  }
  .card--front { left: 73px; }
  .card--back { left: 615px; }

  /* front */
  .front-brand {
    position: absolute;
    left: 34px;
    top: 27px;
    line-height: 1;
  }
  .brand-name {
    color: var(--lime);
    font-weight: 700;
    font-size: 17px;
    letter-spacing: 1.5px;
    text-transform: uppercase;
  }
  .brand-region {
    color: var(--teal);
    font-weight: 700;
    font-size: 10px;
    letter-spacing: 1.6px;
    text-transform: uppercase;
    margin-top: 3px;
  }
  .wave-art {
    position: absolute;
    left: 0;
    top: 0;
    width: 513px;
    height: 296px;
  }

  /* back */
  .back-logo {
    position: absolute;
    left: 0;
    width: 256px;
    top: 104px;
    display: flex;
    flex-direction: column;
    align-items: center;
    gap: 10px;
  }
  .back-logo .brand-mark {
    width: 58px;
    height: 58px;
    border-radius: 50%;
    background: var(--teal);
  }
  .back-logo .brand-name { font-size: 20px; letter-spacing: 2px; }
  .back-logo .brand-region { font-size: 11px; margin-top: -6px; }
  .divider {
    position: absolute;
    left: 256px;
    top: 62px;
    width: 1.5px;
    height: 178px;
    background: var(--lime);
  }
  .contact {
    position: absolute;
    left: 293px;
    top: 60px;
    color: var(--ink);
  }
  .contact-name {
    color: var(--lime);
    font-size: 16px;
    font-weight: 400;
    letter-spacing: 0.3px;
    text-transform: uppercase;
    line-height: 1.1;
  }
  .contact-role {
    font-size: 12px;
    margin-top: 3px;
  }
  .contact-list { list-style: none; margin-top: 16px; font-size: 12px; }
  .contact-list li {
    display: flex;
    align-items: flex-start;
    gap: 6px;
    line-height: 18.5px;
  }
  .contact-list li.gap { margin-top: 10px; }
  .icon { width: 11px; height: 11px; flex: none; margin-top: 4px; fill: var(--lime); }
</style>
</head>
<body>

<section class="card card--front">
  <svg class="wave-art" viewBox="0 0 513 296" role="img" aria-label="Flowing lime and teal striped wave pattern crossing the card">
    <defs>
      <linearGradient id="waveTone" x1="0" y1="1" x2="1" y2="0">
        <stop offset="0" stop-color="#00a88e"/>
        <stop offset="0.5" stop-color="#6fbd62"/>
        <stop offset="1" stop-color="#acd036"/>
      </linearGradient>
    </defs>
    <path d="M0 140 C60 110 120 120 150 80 C200 20 300 10 340 0 L513 0 L513 190 C460 200 400 230 330 260 C260 290 180 296 120 296 L0 296 Z" fill="url(#waveTone)" opacity="0.85"/>
  </svg>
  <div class="front-brand">
    <div class="brand-name">Kin Dart</div>
    <div class="brand-region">Hong Kong</div>
  </div>
</section>

<section class="card card--back">
  <div class="back-logo">
    <span class="brand-mark"></span>
    <div class="brand-name">Kin Dart</div>
    <div class="brand-region">Hong Kong</div>
  </div>
  <span class="divider"></span>
  <div class="contact">
    <h1 class="contact-name">Ravel Oskarin</h1>
    <p class="contact-role">managing director</p>
    <ul class="contact-list">
      <li>
        <svg class="icon" viewBox="0 0 12 12"><path d="M3 1 L5 3.5 L4 5 C4.6 6.4 5.6 7.4 7 8 L8.5 7 L11 9 L9.8 11 C5 10.6 1.4 7 1 2.2 Z"/></svg>
        852 314 27 60
      </li>
      <li>
        <svg class="icon" viewBox="0 0 12 12"><path d="M3 0.5 H9 V11.5 H3 Z M4 1.5 V9 H8 V1.5 Z"/><circle cx="6" cy="10.2" r="0.6"/></svg>
        852 906 41 18
      </li>
      <li>
        <svg class="icon" viewBox="0 0 12 12"><path d="M0.5 2.5 H11.5 V9.5 H0.5 Z"/><path d="M0.5 2.5 L6 6.5 L11.5 2.5" fill="none" stroke="#474747" stroke-width="1"/></svg>
        roskarin@kin-dart.com
      </li>
      <li class="gap">
        <svg class="icon" viewBox="0 0 12 12"><path d="M6 0.5 C8.4 0.5 10 2.2 10 4.4 C10 7 6 11.5 6 11.5 C6 11.5 2 7 2 4.4 C2 2.2 3.6 0.5 6 0.5 Z M6 3 A1.4 1.4 0 1 0 6 5.8 A1.4 1.4 0 1 0 6 3 Z"/></svg>
        <span>27 Harbour Lane, Eastvale<br>Hong Kong 54321</span>
      </li>
      <li>
        <svg class="icon" viewBox="0 0 12 12"><circle cx="6" cy="6" r="5.3"/><path d="M0.7 6 H11.3 M6 0.7 C3.5 3.5 3.5 8.5 6 11.3 M6 0.7 C8.5 3.5 8.5 8.5 6 11.3" fill="none" stroke="#474747" stroke-width="0.8"/></svg>
        www.kin-dart.com
      </li>
    </ul>
  </div>
</section>

</body>
</html>
```